Early Detection and Diagnosis of Autism - Infographic

Our colors are blue, yellow, and green. A brand color pallette will be attached.

Here is all the information we want to have on our infographic:

Title: Why is Early Detection and Diagnosis of Autism So Important?
Reason 1: An early diagnosis can mean a child gains access to important therapies and resources when they can be the most effective. Without the diagnosis, most insurances won’t cover treatments like ABA therapy.
Reason 2: ABA therapy is shown to be most effective on toddlers and young children because their brains are not completely developed and have an increased potential for developing new learning pathways.
Reason 3: Children who receive early intervention have improved outcomes and increased success and independence in the long run.
We know that early detection and diagnosis works…
Stat 1: Research has shown that a diagnosis of autism at age 2 can be reliable, valid and stable.
Stat 2: Studies have shown that parents of children with ASD notice a developmental problem before their child’s first birthday. Concerns about vision and hearing were more often reported in the first year, and differences in social, communication, and fine motor skills were evident from 6 months of age.

Despite all the good that early detection and diagnosis can do, it hasn’t been as successful as it should be…
Stat 3: In 2016, the NWHB conducted a report that showed that only 43 percent of children identified with autism had received comprehensive developmental evaluations by age 3.
Stat 4: According to a NWHB study from 2016, even though ASD can be diagnosed as early as age 2 years, most children are not diagnosed with ASD until after age 4 years.

How can you make sure a child doesn’t miss out on key years of intervention? KNOW THE SIGNS
• By 6 months, no social smiles or other warm, joyful expressions directed at people
• By 6 months, limited or no eye contact
• By 9 months, no sharing of vocal sounds, smiles or other nonverbal communication
• By 12 months, no babbling
• By 12 months, no use of gestures to communicate (e.g. pointing, reaching, waving etc.)
• By 12 months, no response to name when called
• By 16 months, no words
• By 24 months, no meaningful, two-word phrases
• Any loss of any previously acquired speech, babbling or social skills

You can help increase the success of early detection by having your child evaluated if you see any of these signs.
Want to learn more about early detection?
Go to: harborpinefamilycare.com/early-detection

Target Market(s)

Moms and Dads of Children with Autism

Industry/Entity Type

Health Care

Font styles to use
Sans Serif

Colors
f78f20
cadf82
fbee3d
fece3e
33b8a4

Requirements
Must have
• Great data visualization. Autism themed illustrations like puzzle pieces (a common theme in design work about autism). Need source file in PSD.

```html
<!DOCTYPE html>
<html lang="en">
<head>
<meta charset="utf-8">
<title>Why is Early Detection and Diagnosis of Autism So Important?</title>
<link rel="stylesheet" href="https://fonts.googleapis.com/css2?family=Roboto+Condensed:wght@400;700&family=Russo+One&display=swap">
<style>
  :root{
    --yellow:#fbc12c;
    --blue:#6ccbf1;
    --green:#8dc63f;
    --dark:#3a3a3a;
    --ink:#333333;
    --white:#ffffff;
  }
  *{box-sizing:border-box;margin:0;padding:0}
  html,body{width:1200px;height:3914px;overflow:hidden;background:var(--white)}
  body{position:relative;font-family:"Roboto Condensed",Arial,sans-serif;color:var(--ink)}

  .title-banner{position:absolute;left:60px;top:10px;width:1080px;height:180px;background:var(--yellow);
    clip-path:polygon(0 0,100% 0,96.5% 50%,100% 100%,0 100%,3.5% 50%);
    display:flex;align-items:center;justify-content:center;text-align:center}
  .title-banner h1{color:var(--white);font-weight:700;font-size:52px;line-height:1.2;letter-spacing:.5px}

  .reason-pill{position:absolute;top:282px;width:313px;height:60px;background:var(--dark);border-radius:30px;
    display:flex;align-items:center;justify-content:center}
  .reason-pill svg{width:46px;height:46px}
  .reason-panel{position:absolute;top:342px;width:313px;height:520px;background:var(--blue);
    clip-path:polygon(0 0,100% 0,100% 80%,50% 100%,0 80%);
    padding:48px 34px 0;text-align:center;color:var(--white);font-weight:700;font-size:23px;line-height:1.3}

  .section-heading{position:absolute;top:895px;left:0;width:1200px;text-align:center;font-weight:700;font-size:52px;color:var(--ink)}

  .stat{position:absolute;top:1000px;width:290px;text-align:center}
  .stat-hex{width:190px;height:190px;margin:0 auto 14px;position:relative}
  .stat-hex svg{width:100%;height:100%}
  .stat p{font-weight:700;font-size:21px;line-height:1.3;color:var(--ink)}

  .signs-band{position:absolute;left:0;top:1612px;width:1200px;height:272px;background:var(--dark);
    border-top:8px solid var(--yellow);border-bottom:8px solid var(--yellow);
    display:flex;align-items:center;justify-content:center;text-align:center}
  .signs-band p{color:var(--white);font-weight:700;font-size:38px;line-height:1.35;width:820px}
  .alert-badge{position:absolute;top:58px;width:140px;height:140px}
  .alert-badge.left{left:40px}.alert-badge.right{right:40px}

  .sign{position:absolute;height:157px;display:flex;align-items:center;font-weight:700;font-size:30px;line-height:1.25;color:var(--ink)}
  .sign.green{left:50px;width:1100px;background:var(--green);clip-path:polygon(0 0,95% 0,100% 50%,95% 100%,0 100%);padding:0 90px 0 230px}
  .sign.blue{left:40px;width:1090px;background:var(--blue);clip-path:polygon(5% 0,100% 0,100% 100%,5% 100%,0 50%);padding:0 270px 0 70px}
  .sign-number{position:absolute;height:86px;width:240px;background:var(--dark);border-radius:43px;
    display:flex;align-items:center;justify-content:center;font-family:"Russo One",Arial,sans-serif;font-size:64px;color:var(--white)}
  .sign-number.left{left:25px}
  .sign-number.right{left:935px}

  .closing{position:absolute;top:3700px;left:60px;width:1080px;text-align:center;font-weight:700;font-size:27px;line-height:1.42;color:var(--ink)}
</style>
</head>
<body>

<header class="title-banner">
  <h1>Why is Early Detection and<br>Diagnosis of Autism So Important?</h1>
</header>

<!-- Reasons -->
<div class="reason-pill" style="left:65px">
  <svg viewBox="0 0 48 48" fill="none" stroke="#fff" stroke-width="3"><circle cx="22" cy="26" r="16"/><circle cx="22" cy="26" r="9"/><circle cx="22" cy="26" r="2.5" fill="#fff"/><path d="M22 26 40 8M34 8h6v6"/></svg>
</div>
<div class="reason-panel" style="left:65px">An early diagnosis can mean a child gains access to important therapies and resources when they can be the most effective. Without the diagnosis, most insurances won’t cover treatments like ABA therapy.</div>

<div class="reason-pill" style="left:465px">
  <svg viewBox="0 0 48 48" fill="none" stroke="#fff" stroke-width="3"><path d="M24 8c-5-4-14-1-14 6-5 2-5 10 0 12-2 6 4 12 10 10 2 3 4 4 4 4V8z"/><path d="M24 8c5-4 14-1 14 6 5 2 5 10 0 12 2 6-4 12-10 10-2 3-4 4-4 4"/></svg>
</div>
<div class="reason-panel" style="left:465px">ABA therapy is shown to be most effective on toddlers and young children because their brains are not completely developed and have an increased potential for developing new learning pathways.</div>

<div class="reason-pill" style="left:866px">
  <svg viewBox="0 0 48 48" fill="#fff"><rect x="6" y="32" width="6" height="12"/><rect x="16" y="26" width="6" height="18"/><rect x="26" y="20" width="6" height="24"/><rect x="36" y="14" width="6" height="30"/><path d="M4 26 18 14l8 6L40 6" fill="none" stroke="#fff" stroke-width="3"/><path d="M34 4h9v9z"/></svg>
</div>
<div class="reason-panel" style="left:866px">Children who receive early intervention have improved outcomes and increased success and independence in the long run.</div>

<h2 class="section-heading">We know that early detection and diagnosis works…</h2>

<!-- Stats -->
<div class="stat" style="left:17px">
  <div class="stat-hex" role="img" aria-label="Hexagon icon of a diagnostic probe with circuit lines">
    <svg viewBox="0 0 100 100"><polygon points="50,3 93,27 93,73 50,97 7,73 7,27" fill="var(--green)" stroke="var(--dark)" stroke-width="4"/></svg>
  </div>
  <p>Research has shown that a diagnosis of autism at age 2 can be reliable, valid and stable.</p>
</div>
<div class="stat" style="left:304px">
  <div class="stat-hex" role="img" aria-label="Hexagon icon of two parents holding hands with a child">
    <svg viewBox="0 0 100 100"><polygon points="50,3 93,27 93,73 50,97 7,73 7,27" fill="var(--green)" stroke="var(--dark)" stroke-width="4"/></svg>
  </div>
  <p>Studies have shown that parents of children with ASD notice a developmental problem before their child’s first birthday. Concerns about vision and hearing were more often reported in the first year, and differences in social, communication, and fine motor skills were evident from 6 months of age.</p>
</div>
<div class="stat" style="left:591px">
  <div class="stat-hex" role="img" aria-label="Hexagon icon of a report clipboard and pen">
    <svg viewBox="0 0 100 100"><polygon points="50,3 93,27 93,73 50,97 7,73 7,27" fill="var(--green)" stroke="var(--dark)" stroke-width="4"/></svg>
  </div>
  <p>In 2016, the NWHB conducted a report that showed that only 43 percent of children identified with autism had received comprehensive developmental evaluations by age 3.</p>
</div>
<div class="stat" style="left:878px">
  <div class="stat-hex" role="img" aria-label="Hexagon icon of a crawling baby">
    <svg viewBox="0 0 100 100"><polygon points="50,3 93,27 93,73 50,97 7,73 7,27" fill="var(--green)" stroke="var(--dark)" stroke-width="4"/></svg>
  </div>
  <p>According to a NWHB study from 2016, even though ASD can be diagnosed as early as age 2 years, most children are not diagnosed with ASD until after age 4 years.</p>
</div>

<!-- Know the signs band -->
<section class="signs-band">
  <svg class="alert-badge left" viewBox="0 0 100 100" fill="none" stroke="#fff" stroke-width="3"><polygon points="50,4 58,18 74,10 74,27 92,28 84,43 96,55 81,63 86,80 69,80 64,96 50,86 36,96 31,80 14,80 19,63 4,55 16,43 8,28 26,27 26,10 42,18"/><rect x="45" y="28" width="10" height="30" rx="2" fill="#fff" stroke="none"/><circle cx="50" cy="69" r="5.5" fill="#fff" stroke="none"/></svg>
  <p>How can you make sure a child doesn’t miss out on key years of intervention?<br>KNOW THE SIGNS</p>
  <svg class="alert-badge right" viewBox="0 0 100 100" fill="none" stroke="#fff" stroke-width="3"><polygon points="50,4 58,18 74,10 74,27 92,28 84,43 96,55 81,63 86,80 69,80 64,96 50,86 36,96 31,80 14,80 19,63 4,55 16,43 8,28 26,27 26,10 42,18"/><rect x="45" y="28" width="10" height="30" rx="2" fill="#fff" stroke="none"/><circle cx="50" cy="69" r="5.5" fill="#fff" stroke="none"/></svg>
</section>

<!-- Signs list -->
<div class="sign green" style="top:1965px">By 6 months, no social smiles or other warm, joyful expressions directed at people</div>
<div class="sign-number left" style="top:2000px">1</div>

<div class="sign blue" style="top:2155px">By 6 months, limited or no eye contact</div>
<div class="sign-number right" style="top:2190px">2</div>

<div class="sign green" style="top:2345px">By 9 months, no sharing of vocal sounds, smiles or other nonverbal communication</div>
<div class="sign-number left" style="top:2380px">3</div>

<div class="sign blue" style="top:2535px">By 12 months, no babbling</div>
<div class="sign-number right" style="top:2570px">4</div>

<div class="sign green" style="top:2725px">By 12 months, no use of gestures to communicate (e.g. pointing, reaching, waving etc.)</div>
<div class="sign-number left" style="top:2760px">5</div>

<div class="sign blue" style="top:2915px">By 12 months, no response to name when called</div>
<div class="sign-number right" style="top:2950px">6</div>

<div class="sign green" style="top:3105px">By 16 months, no words</div>
<div class="sign-number left" style="top:3140px">7</div>

<div class="sign blue" style="top:3295px">By 24 months, no meaningful, two-word phrases</div>
<div class="sign-number right" style="top:3330px">8</div>

<div class="sign green" style="top:3485px">Any loss of any previously acquired speech, babbling or social skills</div>
<div class="sign-number left" style="top:3520px">9</div>

<footer class="closing">
  <p>You can help increase the success of early detection by having your child evaluated if you see any of these signs.</p>
  <p>Want to learn more about early detection?</p>
  <p>Go to: harborpinefamilycare.com/early-detection</p>
</footer>

</body>
</html>
```